Certificate Design for Employee Loyalty

We're a digital marketing agency in Australia (www.brightkitestudio.com.au) and we're looking to create a design for a certificate to celebrate employees who reach 5 years with us (we have a few coming up soon).
Ideally we'd want something that captures our funky, digital agency culture (see our Facebook page www.facebook.com/brightkitestudio for what we mean) and not be too "corporatey"
A4 portrait or landscape designs would be awesome, with spots for employee's name, a brief 2-3 line message and a design that reflects our culture and the 5 year milestone for the employee.
Any questions, please post!
Target Market(s)
Digital marketing employees.

```html
<!DOCTYPE html>
<html lang="en">
<head>
<meta charset="utf-8">
<title>Five Year Certificate – Bright Kite Studio</title>
<link rel="stylesheet" href="https://fonts.googleapis.com/css2?family=Pinyon+Script&family=Lato:wght@300&family=Open+Sans:wght@300&display=swap">
<style>
  :root {
    --band-top: #6fd0d8;
    --band-bottom: #1c6a82;
    --swoosh: #3a3137;
    --panel-white: #ffffff;
    --panel-blue: #bcdcf7;
    --ink-teal: #1f6b82;
    --ghost-cyan: #c4ecf4;
    --ghost-grey: #eef1f3;
    --rule: #3a3a3a;
    --ring-blue: #2b86dc;
    --logo-black: #111417;
    --logo-text: #ffffff;
  }
  * { margin: 0; padding: 0; box-sizing: border-box; }
  html, body { width: 1200px; height: 848px; overflow: hidden; background: #ffffff; }
  .certificate { position: relative; width: 1200px; height: 848px; overflow: hidden; }
  .frame { position: absolute; inset: 0; }
  .script { font-family: "Pinyon Script", cursive; position: absolute; white-space: nowrap; }
  .title-ghost { left: 95px; top: 88px; font-size: 100px; color: var(--ghost-grey); }
  .title { left: 62px; top: 40px; font-size: 92px; color: var(--ghost-cyan); }
  .awarded { left: 0; width: 1200px; text-align: center; top: 202px; font-size: 50px; color: var(--ink-teal); }
  .since { left: 344px; top: 541px; font-size: 21px; color: var(--ink-teal); }
  .secretary { left: 886px; top: 716px; font-size: 22px; color: var(--ink-teal); }
  .milestone {
    position: absolute; left: 1026px; top: 48px; width: 128px; height: 128px;
    border-radius: 50%; background: var(--panel-white);
    border: 5px solid var(--ring-blue); box-shadow: 0 0 0 4px #ffffff;
    font-family: "Open Sans", sans-serif; font-weight: 300; color: #2a2a2a;
    font-size: 36px; line-height: 36px; text-align: center; padding-top: 26px;
  }
  .brand-name {
    position: absolute; left: 62px; top: 664px; width: 212px; text-align: center;
    font-family: "Lato", sans-serif; font-weight: 300; font-size: 27px;
    color: var(--logo-text); letter-spacing: 1px;
  }
</style>
</head>
<body>
<main class="certificate">
  <svg class="frame" width="1200" height="848" viewBox="0 0 1200 848">
    <defs>
      <linearGradient id="band" x1="0" y1="0" x2="0" y2="1">
        <stop offset="0" stop-color="var(--band-top)"/>
        <stop offset="1" stop-color="var(--band-bottom)"/>
      </linearGradient>
      <radialGradient id="panel-glow" cx="0.52" cy="0.45" r="0.6">
        <stop offset="0" stop-color="var(--panel-blue)"/>
        <stop offset="0.6" stop-color="#e2effb"/>
        <stop offset="1" stop-color="var(--panel-white)"/>
      </radialGradient>
      <linearGradient id="sky" x1="0" y1="0" x2="1" y2="1">
        <stop offset="0" stop-color="#c9def3"/>
        <stop offset="1" stop-color="#2e4fa3"/>
      </linearGradient>
      <linearGradient id="rings" x1="0" y1="0" x2="1" y2="1">
        <stop offset="0" stop-color="#5f9de0"/>
        <stop offset="1" stop-color="#1f4fb0"/>
      </linearGradient>
      <radialGradient id="ornament-fill" cx="0.5" cy="0.5" r="0.5">
        <stop offset="0" stop-color="var(--ink-teal)" stop-opacity="0.55"/>
        <stop offset="1" stop-color="var(--ink-teal)" stop-opacity="0"/>
      </radialGradient>
    </defs>

    <rect class="outer-edge" x="16" y="16" width="1168" height="816" fill="#bfeff4"/>
    <rect class="band" x="22" y="22" width="1156" height="804" fill="url(#band)"/>
    <rect class="mat" x="40" y="38" width="1120" height="772" fill="#ffffff"/>
    <rect class="swoosh" x="48" y="45" width="1104" height="758" fill="var(--swoosh)"/>
    <path class="panel" fill="url(#panel-glow)"
      d="M48,45 L876,45 C990,50 1110,70 1132,170 C1142,230 1146,300 1148,360 L1150,770 Q1150,792 1124,794 C900,802 620,792 380,757 L95,745 C72,520 60,260 48,45 Z"/>

    <!-- title rule with tapered ends -->
    <g class="name-rule" fill="var(--ink-teal)">
      <rect x="192" y="332" width="814" height="2.5"/>
      <rect x="215" y="340" width="770" height="1.2"/>
      <path d="M190,336 C205,338 225,342 240,348 L215,344 Z"/>
      <path d="M1008,336 C993,338 973,342 958,348 L983,344 Z"/>
    </g>

    <!-- message lines with bracket curves -->
    <g class="message-lines" stroke="var(--rule)" stroke-width="1.2">
      <line x1="277" y1="398" x2="922" y2="398"/>
      <line x1="283" y1="432" x2="915" y2="432"/>
      <line x1="287" y1="466" x2="910" y2="466"/>
      <line x1="291" y1="500" x2="907" y2="500"/>
    </g>
    <g class="message-brackets" fill="none" stroke="#8a9aa3" stroke-width="2">
      <path d="M262,400 C256,430 262,475 272,503"/>
      <path d="M270,404 C266,430 270,470 278,500"/>
      <path d="M938,400 C944,430 938,475 928,503"/>
      <path d="M930,404 C934,430 930,470 922,500"/>
    </g>

    <line class="since-line" x1="448" y1="563" x2="832" y2="563" stroke="var(--rule)" stroke-width="1.2"/>
    <ellipse class="ornament" role="img" aria-label="Small flourish divider" cx="600" cy="630" rx="62" ry="10" fill="url(#ornament-fill)"/>
    <line class="signature-line" x1="735" y1="714" x2="1118" y2="714" stroke="var(--rule)" stroke-width="1.2"/>

    <!-- brand circles -->
    <circle cx="106" cy="560" r="58" fill="#ffffff"/>
    <circle class="photo-office" role="img" aria-label="Photo of the studio building sign against a blue sky" cx="106" cy="560" r="50" fill="url(#sky)" stroke="var(--swoosh)" stroke-width="5"/>
    <circle cx="168" cy="692" r="116" fill="#ffffff"/>
    <circle class="brand-badge" cx="168" cy="692" r="106" fill="var(--logo-black)" stroke="var(--ring-blue)" stroke-width="6"/>
    <circle cx="314" cy="733" r="66" fill="#ffffff"/>
    <circle class="photo-pattern" role="img" aria-label="Abstract photo of gold rings on blue" cx="314" cy="733" r="56" fill="url(#rings)" stroke="var(--swoosh)" stroke-width="5"/>
  </svg>

  <div class="script title-ghost">Certificate</div>
  <div class="script title">Certificate</div>
  <div class="script awarded">Awarded to</div>
  <div class="script since">Since today</div>
  <div class="script secretary">Secretary</div>

  <div class="milestone">Five<br>Year</div>
  <div class="brand-name">Bright Kite Studio</div>
</main>
</body>
</html>
```